Professional PowerPoint Template for Data Reports, Presentations

We are a small leadership coaching/consulting firm and would like to update our PowerPoint template that we use with our clients, who are typically mid-senior level company professionals. I've attached a sample Powerpoint as well as our branding guide. The cover page is what needs the most work - just doesn't look current/professional enough. We do want to keep the pages after that clean, with come color but enough space for text and graphics.
Target Market(s)
Senior mgmt and HR executives in small-mid sized companies
Font styles to use
Sans Serif
Requirements
Must have
- Professional
- Clean
- Tied to company color scheme/logo
Nice to have
- Our title pages don't usually have many words on them; we'd like a design that has a lot of color - probably still using mainly our blue but accented with other colors.
- Need simple but smart looking pages after cover with lot of space; mostly we have text on the slides. Currently this is often in bullet point style, but we could probably upgrade the options there.
Should not have
- Anything that looks like a marketing style, as we typically use these with our current clients to share results of data collected, project plans, etc.

```html
<!DOCTYPE html>
<html lang="en">
<head>
<meta charset="utf-8">
<title>Halvern Presentation Template – Slide Overview</title>
<link href="https://fonts.googleapis.com/css2?family=Open+Sans:wght@300;400;600;700;800&display=swap" rel="stylesheet">
<style>
:root{
  --blue:#2c5a93;
  --blue-dark:#1f4676;
  --navy:#1d4a6e;
  --orange:#ef7b4d;
  --teal:#6db5a1;
  --lavender:#dcd6ea;
  --ink:#3d3d3d;
  --canvas:#a9a6a6;
  --white:#ffffff;
}
*{box-sizing:border-box;margin:0;padding:0}
html,body{width:1200px;height:1200px;overflow:hidden;background:var(--canvas)}
body{font-family:"Open Sans",Arial,sans-serif;color:var(--ink)}
.board{display:grid;grid-template-columns:repeat(4,280px);grid-template-rows:repeat(5,210px);column-gap:16px;row-gap:22px;padding:31px 16px}
.slide{position:relative;width:280px;height:210px;background:var(--white);overflow:hidden}
.slide-title{position:absolute;left:13px;top:6px;font-size:10.5px;font-weight:700;color:var(--blue);letter-spacing:.1px}
.footer{position:absolute;left:8px;right:0;bottom:3px;height:9px;background:var(--blue);display:flex;align-items:center;border-radius:0 5px 5px 0}
.footer .brand{font-size:5px;font-weight:700;color:var(--white);letter-spacing:1.2px;margin-left:6px;display:flex;align-items:center;gap:3px}
.footer .brand::before{content:"";width:5px;height:5px;border-radius:50%;background:var(--white)}
.footer .web{position:absolute;left:50%;transform:translateX(-50%);font-size:3px;color:var(--white)}
.footer .page{position:absolute;right:0;top:0;height:9px;width:16px;background:var(--orange);border-radius:5px;font-size:3px;color:var(--white);display:flex;align-items:center;justify-content:center}
.lorem{font-size:3.6px;line-height:1.4;color:var(--ink)}
.lorem-w{font-size:5.4px;line-height:1.55;color:var(--white)}
.caps-orange{font-size:5.3px;line-height:1.55;color:var(--orange);text-transform:uppercase}
.photo{position:absolute}
.abs{position:absolute}
.member{position:absolute;text-align:center;width:60px}
.member .face{border-radius:50%;margin:0 auto;background:radial-gradient(circle at 50% 45%,#8a8a8a,#3e4248 70%)}
.member .face.light{background:radial-gradient(circle at 50% 45%,#e9dcc4,#b7a88a 70%)}
.member .nm{font-size:5px;color:var(--orange);margin-top:4px}
.member .ps{font-size:3.2px;color:#555;margin-top:2px}
</style>
</head>
<body>
<main class="board">

<!-- 1 CEO -->
<section class="slide">
  <div class="abs" style="left:0;top:0;width:75px;height:210px;background:var(--blue)"></div>
  <div class="abs" style="left:11px;top:40px;font-size:6px;font-weight:700;color:var(--white);letter-spacing:1px">HALVERN</div>
  <div class="abs" style="left:11px;top:85px;font-size:8.6px;line-height:1.3;font-weight:800;color:var(--white)">MEET OUR<br>CEO/<br>PRESIDENT<br>DIRECTOR/<br>COUNTRY<br>MANAGER</div>
  <div class="photo" role="img" aria-label="Portrait photo of the company leader in a suit" style="left:75px;top:0;width:113px;height:210px;background:linear-gradient(90deg,#d9d5cf,#b9b2a8 45%,#e6e2dc)"></div>
  <div class="abs" style="left:199px;top:48px;font-size:7.5px;color:var(--orange)">NAME</div>
  <div class="abs lorem" style="left:199px;top:68px;width:76px;font-size:4.6px;line-height:1.45">Lorem ipsum dolor sit amet, consectetur adipiscing elit, sed do eiusmod tempor incididunt ut labore et dolore magna aliqua.<br><br>Ut enim ad minim veniam, quis nostrud exercitation ullamco laboris nisi ut aliquip ex ea commodo consequat.</div>
  <svg class="abs" style="left:204px;top:176px" width="70" height="12" viewBox="0 0 70 12" fill="#ef7b4d">
    <circle cx="5" cy="3" r="2.6"/><path d="M0 11 Q5 4 10 11Z"/>
    <rect x="28" y="1" width="4" height="3"/><rect x="23" y="8" width="4" height="3"/><rect x="28" y="8" width="4" height="3"/><rect x="33" y="8" width="4" height="3"/><path d="M25 8V6h10v2M30 4v4" stroke="#ef7b4d" stroke-width=".8" fill="none"/>
    <rect x="51" y="4" width="10" height="7" rx="1"/><rect x="54" y="2" width="4" height="2.5" fill="none" stroke="#ef7b4d" stroke-width=".8"/>
  </svg>
  <div class="footer" style="left:265px;background:none"><span class="page" style="right:0">31</span></div>
</section>

<!-- 2 team -->
<section class="slide">
  <h2 class="slide-title">MEET OUR TEAM</h2>
  <p class="abs lorem" style="left:33px;top:42px;width:200px">Lorem ipsum dolor sit amet, consectetur adipiscing elit, sed do eiusmod tempor incididunt ut labore et dolore magna aliqua. Ut enim ad minim veniam, quis nostrud exercitation ullamco laboris nisi ut aliquip ex ea commodo consequat.</p>
  <div class="member" style="left:24px;top:74px"><div class="face" style="width:55px;height:55px" role="img" aria-label="Team member portrait"></div><div class="nm">Name</div><div class="ps">Position</div></div>
  <div class="member" style="left:110px;top:74px"><div class="face" style="width:55px;height:55px" role="img" aria-label="Team member portrait"></div><div class="nm">Name</div><div class="ps">Position</div></div>
  <div class="member" style="left:195px;top:74px"><div class="face" style="width:55px;height:55px" role="img" aria-label="Team member portrait"></div><div class="nm">Name</div><div class="ps">Position</div></div>
  <div class="footer"><span class="brand">HALVERN</span><span class="web">www.halvernpartners.com</span><span class="page">32</span></div>
</section>

<!-- 3 team 6 -->
<section class="slide">
  <h2 class="slide-title">MEET OUR TEAM</h2>
  <div class="member" style="left:27px;top:35px"><div class="face" style="width:44px;height:44px" role="img" aria-label="Team member portrait"></div><div class="nm">Name</div><div class="ps">Position</div></div>
  <div class="member" style="left:110px;top:35px"><div class="face light" style="width:44px;height:44px" role="img" aria-label="Team member portrait"></div><div class="nm">Name</div><div class="ps">Position</div></div>
  <div class="member" style="left:190px;top:35px"><div class="face" style="width:44px;height:44px" role="img" aria-label="Team member portrait"></div><div class="nm">Name</div><div class="ps">Position</div></div>
  <div class="member" style="left:27px;top:113px"><div class="face light" style="width:44px;height:44px" role="img" aria-label="Team member portrait"></div><div class="nm">Name</div><div class="ps">Position</div></div>
  <div class="member" style="left:110px;top:113px"><div class="face" style="width:44px;height:44px" role="img" aria-label="Team member portrait"></div><div class="nm">Name</div><div class="ps">Position</div></div>
  <div class="member" style="left:190px;top:113px"><div class="face light" style="width:44px;height:44px" role="img" aria-label="Team member portrait"></div><div class="nm">Name</div><div class="ps">Position</div></div>
  <div class="footer"><span class="brand">HALVERN</span><span class="web">www.halvernpartners.com</span><span class="page">33</span></div>
</section>

<!-- 4 section break -->
<section class="slide">
  <h2 class="slide-title">SLIDE WITH IMAGE</h2>
  <div class="photo" role="img" aria-label="Photo of colleagues stacking hands together" style="left:0;top:29px;width:280px;height:156px;background:linear-gradient(120deg,#f2f2f2,#cfcfcf 45%,#ededed)"></div>
  <div class="abs" style="left:103px;top:77px;width:177px;height:62px;background:linear-gradient(90deg,var(--blue),var(--navy));border-radius:31px 0 0 31px;display:flex;align-items:center;padding-left:52px;font-size:12px;font-weight:400;color:var(--white)">SECTION BREAK</div>
  <div class="footer"><span class="brand">HALVERN</span><span class="web">www.halvernpartners.com</span><span class="page">34</span></div>
</section>

<!-- 5 office -->
<section class="slide">
  <h2 class="slide-title">SLIDE WITH IMAGE</h2>
  <div class="photo" role="img" aria-label="Photo of an empty modern meeting room" style="left:0;top:23px;width:280px;height:162px;background:linear-gradient(180deg,#8f8c88,#c9c6c0 45%,#5a4a3c)"></div>
  <div class="abs" style="left:18px;top:23px;width:79px;height:130px;background:var(--orange);border-radius:0 0 40px 40px;padding:18px 9px">
    <p class="lorem-w">Lorem ipsum dolor sit amet, consectetur adipiscing elit, sed do eiusmod tempor incididunt ut labore et dolore magna aliqua.</p>
  </div>
  <div class="footer"><span class="brand">HALVERN</span><span class="web">www.halvernpartners.com</span><span class="page">35</span></div>
</section>

<!-- 6 hands + gradient -->
<section class="slide">
  <h2 class="slide-title">SLIDE WITH IMAGE</h2>
  <div class="photo" role="img" aria-label="Photo of team members joining hands" style="left:0;top:30px;width:280px;height:156px;background:linear-gradient(120deg,#f4f4f4,#d8d2cc 50%,#f0f0f0)"></div>
  <div class="abs" style="left:159px;top:30px;width:98px;height:156px;background:linear-gradient(180deg,var(--orange),var(--blue) 75%);display:flex;align-items:flex-end;padding:0 6px 32px">
    <p class="lorem-w" style="text-align:center">Lorem ipsum dolor sit amet, consectetur adipiscing elit, sed do eiusmod tempor incididunt ut labore et dolore magna aliqua.</p>
  </div>
  <div class="footer"><span class="brand">HALVERN</span><span class="web">www.halvernpartners.com</span><span class="page">36</span></div>
</section>

<!-- 7 four panels -->
<section class="slide">
  <h2 class="slide-title">SLIDE WITH IMAGE</h2>
  <div class="abs" style="left:5px;top:37px;width:66px;height:124px;background:var(--blue);padding:20px 8px 0">
    <svg width="20" height="14" viewBox="0 0 20 14" style="display:block;margin:0 auto 16px" fill="#fff"><rect x="7" y="0" width="6" height="4"/><rect x="0" y="10" width="5" height="4"/><rect x="7.5" y="10" width="5" height="4"/><rect x="15" y="10" width="5" height="4"/><path d="M2.5 10V7h15v3M10 4v6" stroke="#fff" stroke-width="1" fill="none"/></svg>
    <p class="lorem-w" style="font-size:4.4px">Lorem ipsum dolor sit amet, consectetur adipiscing elit, sed do eiusmod tempor incididunt ut labore et dolore magna aliqua.</p>
  </div>
  <div class="photo" role="img" aria-label="Photo of a glass skyscraper" style="left:73px;top:37px;width:66px;height:124px;background:linear-gradient(160deg,#9fc2ea,#2d5a9c 55%,#14305e)"></div>
  <div class="abs" style="left:141px;top:37px;width:66px;height:124px;background:var(--teal);padding:20px 8px 0">
    <svg width="18" height="14" viewBox="0 0 18 14" style="display:block;margin:0 auto 16px" fill="#fff"><rect x="0" y="9" width="3" height="5"/><rect x="5" y="6" width="3" height="8"/><rect x="10" y="4" width="3" height="10"/><rect x="15" y="1" width="3" height="13"/></svg>
    <p class="lorem-w" style="font-size:4.4px">Lorem ipsum dolor sit amet, consectetur adipiscing elit, sed do eiusmod tempor incididunt ut labore et dolore magna aliqua.</p>
  </div>
  <div class="photo" role="img" aria-label="Photo of a hand touching a digital gear icon" style="left:209px;top:37px;width:66px;height:124px;background:linear-gradient(160deg,#3c4a5a,#1b2129 70%)"></div>
  <div class="footer"><span class="brand">HALVERN</span><span class="web">www.halvernpartners.com</span><span class="page">37</span></div>
</section>

<!-- 8 mosaic -->
<section class="slide">
  <h2 class="slide-title">SLIDE WITH IMAGE</h2>
  <div class="abs" style="left:14px;top:30px;width:65px;height:72px;background:var(--blue);padding:9px 8px">
    <div style="font-size:5px;color:#fff;margin-bottom:6px">LOREM IPSUM</div>
    <p class="lorem-w" style="font-size:3.6px">Lorem ipsum dolor sit amet, consectetur adipiscing elit, sed do eiusmod tempor incididunt ut labore et dolore magna aliqua.</p>
  </div>
  <div class="photo" role="img" aria-label="Photo of clocks over a night city skyline" style="left:81px;top:30px;width:182px;height:72px;background:linear-gradient(90deg,#2c5a93,#3b6a9c 40%,#10203a)"></div>
  <div class="photo" role="img" aria-label="Photo of a person holding a skills concept with icons" style="left:14px;top:104px;width:110px;height:70px;background:linear-gradient(90deg,#2f74b8,#1d4f8c)"></div>
  <div class="abs" role="img" aria-label="Illustration of heads with idea icons" style="left:125px;top:104px;width:55px;height:70px;background:linear-gradient(90deg,var(--orange),#f29a73)"></div>
  <div class="abs" style="left:182px;top:104px;width:66px;height:70px;background:var(--orange);padding:9px 8px">
    <div style="font-size:5px;color:#fff;margin-bottom:6px">LOREM IPSUM</div>
    <p class="lorem-w" style="font-size:3.6px">Lorem ipsum dolor sit amet, consectetur adipiscing elit, sed do eiusmod tempor incididunt ut labore et dolore magna aliqua.</p>
  </div>
  <div class="footer"><span class="brand">HALVERN</span><span class="web">www.halvernpartners.com</span><span class="page">38</span></div>
</section>

<!-- 9 column text -->
<section class="slide">
  <h2 class="slide-title">COLUMN TEXT</h2>
  <div class="abs" style="left:28px;top:39px;width:215px;height:20px;background:var(--orange);padding:2px 3px"><p class="caps-orange" style="color:#fff;font-size:5.2px">Lorem ipsum dolor sit amet, consectetur adipiscing elit, sed do eiusmod tempor incididunt ut labore et dolore magna aliqua.</p></div>
  <div class="abs lorem" style="left:31px;top:71px;width:88px">Lorem ipsum dolor sit amet, consectetur adipiscing elit, sed do eiusmod tempor incididunt ut labore et dolore magna aliqua.<br><br>Ut enim ad minim veniam, quis nostrud exercitation ullamco laboris nisi ut aliquip ex ea commodo consequat.<br><br>Duis aute irure dolor in reprehenderit in voluptate velit esse cillum dolore eu fugiat nulla pariatur.<br><br>Excepteur sint occaecat cupidatat non proident, sunt in culpa qui officia deserunt mollit anim id est laborum.</div>
  <div class="abs lorem" style="left:154px;top:71px;width:88px">Lorem ipsum dolor sit amet, consectetur adipiscing elit, sed do eiusmod tempor incididunt ut labore et dolore magna aliqua.<br><br>Ut enim ad minim veniam, quis nostrud exercitation ullamco laboris nisi ut aliquip ex ea commodo consequat.<br><br>Duis aute irure dolor in reprehenderit in voluptate velit esse cillum dolore eu fugiat nulla pariatur.<br><br>Excepteur sint occaecat cupidatat non proident, sunt in culpa qui officia deserunt mollit anim id est laborum.</div>
  <div class="footer"><span class="brand">HALVERN</span><span class="web">www.halvernpartners.com</span><span class="page">39</span></div>
</section>

<!-- 10 column text labels -->
<section class="slide">
  <h2 class="slide-title">COLUMN TEXT</h2>
  <p class="abs caps-orange" style="left:22px;top:32px;width:220px">Lorem ipsum dolor sit amet, consectetur adipiscing elit, sed do eiusmod tempor incididunt ut labore et dolore magna aliqua.</p>
  <div class="abs" style="left:22px;top:64px;width:240px">
    <div style="background:var(--orange);color:#fff;font-size:3.4px;width:82px;padding:1px 3px;margin-bottom:2px">LOREM IPSUM DOLOR SIT AMET</div>
    <p class="lorem" style="margin-bottom:8px">Lorem ipsum dolor sit amet, consectetur adipiscing elit, sed do eiusmod tempor incididunt ut labore et dolore magna aliqua. Ut enim ad minim veniam, quis nostrud exercitation ullamco laboris nisi ut aliquip ex ea commodo consequat. Duis aute irure dolor in reprehenderit in voluptate velit esse cillum dolore eu fugiat nulla pariatur. Excepteur sint occaecat cupidatat non proident, sunt in culpa qui officia deserunt mollit anim id est laborum.</p>
    <div style="background:var(--orange);color:#fff;font-size:3.4px;width:82px;padding:1px 3px;margin-bottom:2px">LOREM IPSUM DOLOR SIT AMET</div>
    <p class="lorem" style="margin-bottom:8px">Lorem ipsum dolor sit amet, consectetur adipiscing elit, sed do eiusmod tempor incididunt ut labore et dolore magna aliqua. Ut enim ad minim veniam, quis nostrud exercitation ullamco laboris nisi ut aliquip ex ea commodo consequat. Duis aute irure dolor in reprehenderit in voluptate velit esse cillum dolore eu fugiat nulla pariatur. Excepteur sint occaecat cupidatat non proident, sunt in culpa qui officia deserunt mollit anim id est laborum.</p>
    <div style="background:var(--orange);color:#fff;font-size:3.4px;width:82px;padding:1px 3px;margin-bottom:2px">LOREM IPSUM DOLOR SIT AMET</div>
    <p class="lorem">Lorem ipsum dolor sit amet, consectetur adipiscing elit, sed do eiusmod tempor incididunt ut labore et dolore magna aliqua. Ut enim ad minim veniam, quis nostrud exercitation ullamco laboris nisi ut aliquip ex ea commodo consequat. Duis aute irure dolor in reprehenderit in voluptate velit esse cillum dolore eu fugiat nulla pariatur. Excepteur sint occaecat cupidatat non proident, sunt in culpa qui officia deserunt mollit anim id est laborum.</p>
  </div>
  <div class="footer"><span class="brand">HALVERN</span><span class="web">www.halvernpartners.com</span><span class="page">40</span></div>
</section>

<!-- 11 timeline -->
<section class="slide">
  <h2 class="slide-title">TIMELINE HISTORY</h2>
  <svg class="abs" style="left:0;top:0" width="280" height="210" viewBox="0 0 280 210">
    <line x1="0" y1="100" x2="270" y2="100" stroke="#2c5a93" stroke-width="1"/>
    <path d="M270 96 L280 100 L270 104Z" fill="#2c5a93"/>
    <g stroke="#2c5a93" stroke-width=".7" stroke-dasharray="1.5 1" fill="none">
      <line x1="48" y1="40" x2="48" y2="90"/><line x1="108" y1="110" x2="108" y2="163"/>
      <line x1="168" y1="40" x2="168" y2="90"/><line x1="228" y1="110" x2="228" y2="163"/>
    </g>
    <g fill="#dde6f1" stroke="#2c5a93" stroke-width="1"><circle cx="48" cy="100" r="7"/><circle cx="108" cy="100" r="7"/><circle cx="168" cy="100" r="7"/><circle cx="228" cy="100" r="7"/></g>
    <g fill="#2c5a93"><circle cx="48" cy="90" r="1.3"/><circle cx="108" cy="110" r="1.3"/><circle cx="168" cy="90" r="1.3"/><circle cx="228" cy="110" r="1.3"/></g>
    <g font-family="Open Sans, sans-serif" font-weight="700" font-size="8.5" fill="#ef7b4d">
      <text x="36" y="124">2015</text><text x="96" y="86">2016</text><text x="156" y="122">2017</text><text x="216" y="87">2018</text>
    </g>
  </svg>
  <p class="abs lorem" style="left:52px;top:39px;width:62px">Lorem ipsum dolor sit amet, consectetur adipiscing elit, sed do eiusmod tempor incididunt ut labore et dolore magna aliqua.</p>
  <p class="abs lorem" style="left:172px;top:39px;width:62px">Lorem ipsum dolor sit amet, consectetur adipiscing elit, sed do eiusmod tempor incididunt ut labore et dolore magna aliqua.</p>
  <p class="abs lorem" style="left:43px;top:136px;width:62px;text-align:right">Lorem ipsum dolor sit amet, consectetur adipiscing elit, sed do eiusmod tempor incididunt ut labore et dolore magna aliqua.</p>
  <p class="abs lorem" style="left:163px;top:136px;width:62px;text-align:right">Lorem ipsum dolor sit amet, consectetur adipiscing elit, sed do eiusmod tempor incididunt ut labore et dolore magna aliqua.</p>
  <div class="footer"><span class="brand">HALVERN</span><span class="web">www.halvernpartners.com</span><span class="page">41</span></div>
</section>

<!-- 12 timeline band -->
<section class="slide">
  <h2 class="slide-title">TIMELINE HISTORY</h2>
  <svg class="abs" style="left:0;top:0" width="280" height="210" viewBox="0 0 280 210">
    <rect x="0" y="70" width="280" height="59" fill="#2c5a93"/>
    <line x1="0" y1="100" x2="270" y2="100" stroke="#c9d6e8" stroke-width="1"/>
    <path d="M270 96 L280 100 L270 104Z" fill="#c9d6e8"/>
    <g stroke="#2c5a93" stroke-width=".7" stroke-dasharray="1.5 1" fill="none">
      <line x1="48" y1="37" x2="48" y2="70"/><line x1="168" y1="37" x2="168" y2="70"/>
      <line x1="106" y1="129" x2="106" y2="163"/><line x1="226" y1="129" x2="226" y2="163"/>
    </g>
    <g stroke="#c9d6e8" stroke-width=".7" stroke-dasharray="1.5 1"><line x1="48" y1="70" x2="48" y2="90"/><line x1="168" y1="70" x2="168" y2="90"/><line x1="106" y1="110" x2="106" y2="129"/><line x1="226" y1="110" x2="226" y2="129"/></g>
    <g fill="#2c5a93" stroke="#dde6f1" stroke-width="1.2"><circle cx="48" cy="100" r="8"/><circle cx="106" cy="100" r="8"/><circle cx="168" cy="100" r="8"/><circle cx="226" cy="100" r="8"/></g>
    <g font-family="Open Sans, sans-serif" font-weight="700" font-size="8.5" fill="#fff">
      <text x="36" y="124">2015</text><text x="94" y="84">2016</text><text x="156" y="124">2017</text><text x="214" y="84">2018</text>
    </g>
  </svg>
  <p class="abs lorem" style="left:52px;top:36px;width:62px">Lorem ipsum dolor sit amet, consectetur adipiscing elit, sed do eiusmod tempor incididunt ut labore et dolore magna aliqua.</p>
  <p class="abs lorem" style="left:172px;top:36px;width:62px">Lorem ipsum dolor sit amet, consectetur adipiscing elit, sed do eiusmod tempor incididunt ut labore et dolore magna aliqua.</p>
  <p class="abs lorem" style="left:41px;top:134px;width:62px;text-align:right">Lorem ipsum dolor sit amet, consectetur adipiscing elit, sed do eiusmod tempor incididunt ut labore et dolore magna aliqua.</p>
  <p class="abs lorem" style="left:161px;top:134px;width:62px;text-align:right">Lorem ipsum dolor sit amet, consectetur adipiscing elit, sed do eiusmod tempor incididunt ut labore et dolore magna aliqua.</p>
  <div class="footer"><span class="brand">HALVERN</span><span class="web">www.halvernpartners.com</span><span class="page">42</span></div>
</section>

<!-- 13 table -->
<section class="slide">
  <h2 class="slide-title">TABLE STYLE</h2>
  <p class="abs caps-orange" style="left:18px;top:38px;width:220px">Lorem ipsum dolor sit amet, consectetur adipiscing elit, sed do eiusmod tempor incididunt ut labore et dolore magna aliqua.</p>
  <svg class="abs" style="left:15px;top:73px" width="256" height="82" viewBox="0 0 256 82" font-family="Open Sans, sans-serif" font-size="5.6" text-anchor="middle">
    <rect x="0" y="0" width="256" height="27" fill="#2c5a93"/>
    <rect x="0" y="27" width="62" height="55" fill="#6db5a1"/>
    <rect x="62" y="27" width="194" height="27" fill="#dcd6ea"/>
    <rect x="62" y="54" width="194" height="28" fill="#eeeeee"/>
    <g stroke="#fff" stroke-width="1"><line x1="62" y1="0" x2="62" y2="82"/><line x1="101" y1="0" x2="101" y2="82"/><line x1="139" y1="0" x2="139" y2="82"/><line x1="178" y1="0" x2="178" y2="82"/><line x1="217" y1="0" x2="217" y2="82"/><line x1="0" y1="54" x2="256" y2="54"/></g>
    <g fill="#fff" font-weight="700"><text x="82" y="16">Text</text><text x="120" y="16">Text</text><text x="158" y="16">Text</text><text x="197" y="16">Text</text><text x="236" y="16">Text</text><text x="31" y="43">Add Text</text><text x="31" y="70">Add Text</text></g>
    <g fill="#333"><text x="82" y="43">Text</text><text x="120" y="43">Text</text><text x="158" y="43">Text</text><text x="197" y="43">Text</text><text x="236" y="43">Text</text><text x="82" y="70">Text</text><text x="120" y="70">Text</text><text x="158" y="70">Text</text><text x="197" y="70">Text</text><text x="236" y="70">Text</text></g>
  </svg>
  <div class="footer"><span class="brand">HALVERN</span><span class="web">www.halvernpartners.com</span><span class="page">43</span></div>
</section>

<!-- 14 list -->
<section class="slide" style="background:linear-gradient(135deg,#3a78a8,#5a9a9a 50%,#2c5a93)">
  <h2 class="slide-title" style="color:#fff">LIST STYLE</h2>
  <div class="abs" style="left:40px;top:34px;width:220px">
    <div style="display:flex;align-items:center;gap:10px;height:36px"><span style="width:22px;height:22px;border-radius:50%;background:linear-gradient(135deg,#dfe9f2,#8fb0c8);color:var(--blue);font-size:11px;display:flex;align-items:center;justify-content:center;flex:none">1</span><p class="lorem" style="color:#fff;font-size:5px">Lorem ipsum dolor sit amet, consectetur adipiscing elit, sed do eiusmod tempor incididunt ut labore et dolore magna aliqua.</p></div>
    <div style="display:flex;align-items:center;gap:10px;height:36px"><span style="width:22px;height:22px;border-radius:50%;background:linear-gradient(135deg,#dfe9f2,#8fb0c8);color:var(--blue);font-size:11px;display:flex;align-items:center;justify-content:center;flex:none">2</span><p class="lorem" style="color:#fff;font-size:5px">Lorem ipsum dolor sit amet, consectetur adipiscing elit, sed do eiusmod tempor incididunt ut labore et dolore magna aliqua.</p></div>
    <div style="display:flex;align-items:center;gap:10px;height:36px"><span style="width:22px;height:22px;border-radius:50%;background:linear-gradient(135deg,#dfe9f2,#8fb0c8);color:var(--blue);font-size:11px;display:flex;align-items:center;justify-content:center;flex:none">3</span><p class="lorem" style="color:#fff;font-size:5px">Lorem ipsum dolor sit amet, consectetur adipiscing elit, sed do eiusmod tempor incididunt ut labore et dolore magna aliqua.</p></div>
    <div style="display:flex;align-items:center;gap:10px;height:36px"><span style="width:22px;height:22px;border-radius:50%;background:linear-gradient(135deg,#dfe9f2,#8fb0c8);color:var(--blue);font-size:11px;display:flex;align-items:center;justify-content:center;flex:none">4</span><p class="lorem" style="color:#fff;font-size:5px">Lorem ipsum dolor sit amet, consectetur adipiscing elit, sed do eiusmod tempor incididunt ut labore et dolore magna aliqua.</p></div>
  </div>
  <div class="footer"><span class="brand">HALVERN</span><span class="web">www.halvernpartners.com</span><span class="page">44</span></div>
</section>

<!-- 15 multiple bars -->
<section class="slide">
  <h2 class="slide-title">EDITABLE MULTIPLE BARS CHART</h2>
  <svg class="abs" style="left:0;top:0" width="280" height="210" viewBox="0 0 280 210" font-family="Open Sans, sans-serif">
    <g stroke="#e6e6e6" stroke-width=".4">
      <line x1="35" y1="34" x2="250" y2="34"/><line x1="35" y1="50" x2="250" y2="50"/><line x1="35" y1="67" x2="250" y2="67"/><line x1="35" y1="84" x2="250" y2="84"/><line x1="35" y1="101" x2="250" y2="101"/><line x1="35" y1="118" x2="250" y2="118"/>
    </g>
    <g font-size="3.2" fill="#444" text-anchor="end"><text x="32" y="35">50</text><text x="32" y="51">40</text><text x="32" y="68">30</text><text x="32" y="85">20</text><text x="32" y="102">10</text><text x="32" y="119">0</text></g>
    <g>
      <rect x="44" y="64.2" width="7" height="53.8" fill="#2c5a93"/><rect x="51" y="59.2" width="7" height="58.8" fill="#ef7b4d"/><rect x="58" y="81" width="7" height="37" fill="#6db5a1"/><rect x="65" y="87.8" width="7" height="30.2" fill="#dcd6ea"/>
      <rect x="87" y="64.2" width="7" height="53.8" fill="#2c5a93"/><rect x="94" y="76" width="7" height="42" fill="#ef7b4d"/><rect x="101" y="97.8" width="7" height="20.2" fill="#6db5a1"/><rect x="108" y="97.8" width="7" height="20.2" fill="#dcd6ea"/>
      <rect x="130" y="54.2" width="7" height="63.8" fill="#2c5a93"/><rect x="137" y="84.4" width="7" height="33.6" fill="#ef7b4d"/><rect x="144" y="97.8" width="7" height="20.2" fill="#6db5a1"/><rect x="151" y="99.5" width="7" height="18.5" fill="#dcd6ea"/>
      <rect x="173" y="72.6" width="7" height="45.4" fill="#2c5a93"/><rect x="180" y="77.7" width="7" height="40.3" fill="#ef7b4d"/><rect x="187" y="82.7" width="7" height="35.3" fill="#6db5a1"/><rect x="194" y="96.2" width="7" height="21.8" fill="#dcd6ea"/>
      <rect x="216" y="64.2" width="7" height="53.8" fill="#2c5a93"/><rect x="223" y="74.3" width="7" height="43.7" fill="#ef7b4d"/><rect x="230" y="71" width="7" height="47" fill="#6db5a1"/><rect x="237" y="97.8" width="7" height="20.2" fill="#dcd6ea"/>
    </g>
    <g font-size="2.8" fill="#333" text-anchor="middle">
      <text x="47.5" y="62.5">32</text><text x="54.5" y="57.5">35</text><text x="61.5" y="79">22</text><text x="68.5" y="86">18</text>
      <text x="90.5" y="62.5">32</text><text x="97.5" y="74.5">25</text><text x="104.5" y="96">12</text><text x="111.5" y="96">12</text>
      <text x="133.5" y="52.5">38</text><text x="140.5" y="82.5">20</text><text x="147.5" y="96">12</text><text x="154.5" y="98">11</text>
      <text x="176.5" y="71">27</text><text x="183.5" y="76">24</text><text x="190.5" y="81">21</text><text x="197.5" y="94.5">13</text>
      <text x="219.5" y="62.5">32</text><text x="226.5" y="72.5">26</text><text x="233.5" y="69">28</text><text x="240.5" y="96">12</text>
    </g>
    <g font-size="4.2" fill="#333" text-anchor="middle"><text x="58" y="126">January</text><text x="101" y="126">February</text><text x="144" y="126">March</text><text x="187" y="126">April</text><text x="230" y="126">May</text></g>
    <g font-size="5.4" fill="#333">
      <rect x="42" y="142" width="10" height="10" fill="#2c5a93"/><text x="57" y="150">INFORMATION</text>
      <rect x="108" y="142" width="10" height="10" fill="#6db5a1"/><text x="123" y="150">INFORMATION</text>
      <rect x="42" y="166" width="10" height="10" fill="#ef7b4d"/><text x="57" y="174">INFORMATION</text>
      <rect x="108" y="166" width="10" height="10" fill="#dcd6ea"/><text x="123" y="174">INFORMATION</text>
    </g>
  </svg>
  <p class="abs lorem" style="left:182px;top:144px;width:66px;font-size:4.3px">Lorem ipsum dolor sit amet, consectetur adipiscing elit, sed do eiusmod tempor incididunt ut labore et dolore magna aliqua.</p>
  <div class="footer"><span class="brand">HALVERN</span><span class="web">www.halvernpartners.com</span><span class="page">45</span></div>
</section>

<!-- 16 single bar -->
<section class="slide">
  <h2 class="slide-title">EDITABLE SINGLE BAR CHART</h2>
  <svg class="abs" style="left:0;top:0" width="280" height="210" viewBox="0 0 280 210" font-family="Open Sans, sans-serif">
    <defs><linearGradient id="barFade" x1="0" y1="0" x2="0" y2="1"><stop offset="0" stop-color="#ffffff"/><stop offset="1" stop-color="#ffffff" stop-opacity=".15"/></linearGradient></defs>
    <rect x="0" y="35" width="280" height="112" fill="#1d4a6e"/>
    <g stroke="#ffffff" stroke-opacity=".35" stroke-width=".4">
      <line x1="45" y1="42" x2="265" y2="42"/><line x1="45" y1="51" x2="265" y2="51"/><line x1="45" y1="59.5" x2="265" y2="59.5"/><line x1="45" y1="68" x2="265" y2="68"/><line x1="45" y1="76.5" x2="265" y2="76.5"/><line x1="45" y1="85" x2="265" y2="85"/><line x1="45" y1="93.5" x2="265" y2="93.5"/><line x1="45" y1="102" x2="265" y2="102"/><line x1="45" y1="110.5" x2="265" y2="110.5"/><line x1="45" y1="119" x2="265" y2="119"/><line x1="45" y1="127.5" x2="265" y2="127.5"/>
    </g>
    <g font-size="3.6" fill="#fff" text-anchor="end"><text x="41" y="43">96</text><text x="41" y="52">95</text><text x="41" y="60.5">94</text><text x="41" y="69">93</text><text x="41" y="77.5">92</text><text x="41" y="86">91</text><text x="41" y="94.5">90</text><text x="41" y="103">89</text><text x="41" y="111.5">88</text><text x="41" y="120">87</text><text x="41" y="128.5">86</text></g>
    <rect x="60" y="102" width="27" height="25.5" fill="url(#barFade)"/>
    <rect x="108" y="68" width="27" height="59.5" fill="url(#barFade)"/>
    <rect x="156" y="85" width="27" height="42.5" fill="url(#barFade)"/>
    <rect x="204" y="51" width="27" height="76.5" fill="url(#barFade)"/>
    <g font-size="6" fill="#333" text-anchor="middle"><text x="73.5" y="110">89%</text><text x="121.5" y="76">93%</text><text x="169.5" y="93">91%</text><text x="217.5" y="59">95%</text></g>
    <g font-size="4.6" fill="#fff" text-anchor="middle"><text x="73.5" y="139">LOREM IPSUM</text><text x="121.5" y="139">LOREM IPSUM</text><text x="169.5" y="139">LOREM IPSUM</text><text x="217.5" y="139">LOREM IPSUM</text></g>
  </svg>
  <p class="abs lorem" style="left:58px;top:155px;width:190px;font-size:4.2px">Lorem ipsum dolor sit amet, consectetur adipiscing elit, sed do eiusmod tempor incididunt ut labore et dolore magna aliqua.<br><span style="display:block;height:3px"></span>Ut enim ad minim veniam, quis nostrud exercitation ullamco laboris nisi ut aliquip ex ea commodo consequat.</p>
  <div class="footer"><span class="web" style="left:24px;transform:none">www.halvernpartners.com</span><span class="page">46</span></div>
</section>

<!-- 17 donut -->
<section class="slide" style="background:linear-gradient(110deg,#c9795a,#5a6a93 45%,#2c5a93)">
  <h2 class="slide-title" style="color:#fff">EDITABLE CHART</h2>
  <svg class="abs" style="left:0;top:0" width="280" height="210" viewBox="0 0 280 210" font-family="Open Sans, sans-serif">
    <circle cx="84" cy="105" r="60" fill="#1f2d44"/>
    <g transform="rotate(-90 84 105)" fill="none" stroke-width="34">
      <circle cx="84" cy="105" r="40" stroke="#dcd6ea" stroke-dasharray="37.7 251.3"/>
      <circle cx="84" cy="105" r="40" stroke="#ef7b4d" stroke-dasharray="125.7 251.3" stroke-dashoffset="-37.7"/>
      <circle cx="84" cy="105" r="40" stroke="#6db5a1" stroke-dasharray="88 251.3" stroke-dashoffset="-163.4"/>
    </g>
    <circle cx="84" cy="105" r="18" fill="#2c5a93" stroke="#1f2d44" stroke-width="3"/>
    <g font-size="8" font-weight="700" fill="#333"><text x="94" y="82">15%</text><text x="42" y="96">35%</text><text x="96" y="140">50%</text></g>
    <g font-size="5.4" fill="#fff">
      <circle cx="162" cy="60" r="8" fill="#ef7b4d"/><text x="180" y="62">INFORMATION</text>
      <circle cx="162" cy="85" r="8" fill="#6db5a1"/><text x="180" y="87">INFORMATION</text>
      <circle cx="162" cy="111" r="8" fill="#dcd6ea"/><text x="180" y="113">INFORMATION</text>
    </g>
  </svg>
  <p class="abs lorem" style="left:156px;top:134px;width:100px;color:#fff;font-size:4.4px">Lorem ipsum dolor sit amet, consectetur adipiscing elit, sed do eiusmod tempor incididunt ut labore et dolore magna aliqua.</p>
  <div class="footer"><span class="brand">HALVERN</span><span class="web">www.halvernpartners.com</span><span class="page">47</span></div>
</section>

<!-- 18 infographic -->
<section class="slide">
  <h2 class="slide-title">INFOGRAPHIC STYLE</h2>
  <div class="abs" role="img" aria-label="Infographic illustration of overlapping peaks with a flag and a target" style="left:16px;top:30px;width:248px;height:94px;background:linear-gradient(90deg,#c7d3e5,#f4cdbb 50%,#c7d3e5)"></div>
  <p class="abs lorem" style="left:42px;top:148px;width:200px">Lorem ipsum dolor sit amet, consectetur adipiscing elit, sed do eiusmod tempor incididunt ut labore et dolore magna aliqua. Ut enim ad minim veniam, quis nostrud exercitation ullamco laboris nisi ut aliquip ex ea commodo consequat. Duis aute irure dolor in reprehenderit in voluptate velit esse cillum dolore eu fugiat nulla pariatur. Excepteur sint occaecat cupidatat non proident, sunt in culpa qui officia deserunt mollit anim id est laborum.</p>
  <div class="footer"><span class="brand">HALVERN</span><span class="web">www.halvernpartners.com</span><span class="page">48</span></div>
</section>

<!-- 19 thank you photo -->
<section class="slide">
  <div class="photo" role="img" aria-label="Photo of a city skyline at night by the water" style="left:0;top:0;width:280px;height:118px;background:linear-gradient(180deg,#3d5a8a,#1a2438 60%,#0c0f18)"></div>
  <div class="abs" style="left:82px;top:43px;font-size:20px;font-weight:300;color:#fff">THANK YOU</div>
  <div class="abs" style="left:85px;top:124px;font-size:16px;font-weight:700;color:var(--blue);letter-spacing:3px">HALVERN</div>
  <svg class="abs" style="left:85px;top:149px" width="12" height="50" viewBox="0 0 12 50" fill="#2c5a93">
    <path d="M6 0 C2.5 0 1 2.5 1 4.5 C1 7.5 6 11 6 11 C6 11 11 7.5 11 4.5 C11 2.5 9.5 0 6 0Z"/><circle cx="6" cy="4.5" r="1.6" fill="#fff"/>
    <path d="M2 18 L4.5 17 L6 20 L4.5 21.5 Q6 24.5 8.5 25.5 L10 24 L12 26.5 L10 28 Q4 27 1.5 20Z"/>
    <rect x="0" y="37" width="12" height="8" fill="none" stroke="#2c5a93" stroke-width="1"/><path d="M0 37 L6 42 L12 37" fill="none" stroke="#2c5a93" stroke-width="1"/>
  </svg>
  <div class="abs" style="left:104px;top:150px;font-size:5.8px;line-height:16px;color:var(--blue)">P.O. Box 42 , Westfield, MA&nbsp;&nbsp;&nbsp;01085<br>(555) 014-0287<br>info@halvernpartners.com</div>
</section>

<!-- 20 thank you blue -->
<section class="slide" style="background:linear-gradient(180deg,#2c5a93,#2a5690)">
  <div class="photo" role="img" aria-label="Faint city skyline silhouette" style="left:0;top:70px;width:280px;height:140px;background:linear-gradient(180deg,rgba(44,90,147,0),rgba(30,66,112,.7))"></div>
  <div class="abs" style="left:88px;top:26px;font-size:20px;font-weight:300;color:#fff">THANK YOU</div>
  <div class="abs" style="left:93px;top:87px;font-size:13px;font-weight:700;color:#fff;letter-spacing:3px">HALVERN</div>
  <svg class="abs" style="left:92px;top:108px" width="12" height="46" viewBox="0 0 12 46" fill="#fff">
    <path d="M6 0 C2.5 0 1 2.5 1 4.5 C1 7.5 6 11 6 11 C6 11 11 7.5 11 4.5 C11 2.5 9.5 0 6 0Z"/><circle cx="6" cy="4.5" r="1.6" fill="#2c5a93"/>
    <rect x="0" y="17" width="12" height="8" fill="none" stroke="#fff" stroke-width="1"/><path d="M0 17 L6 22 L12 17" fill="none" stroke="#fff" stroke-width="1"/>
    <path d="M2 33 L4.5 32 L6 35 L4.5 36.5 Q6 39.5 8.5 40.5 L10 39 L12 41.5 L10 43 Q4 42 1.5 35Z"/>
  </svg>
  <div class="abs" style="left:111px;top:108px;font-size:5.8px;line-height:16px;color:#fff">P.O. Box 42 , Westfield, MA&nbsp;&nbsp;&nbsp;01085<br>(555) 014-0287<br>info@halvernpartners.com</div>
</section>

</main>
</body>
</html>
```